New Automotive supply business in need of label designs for additive range

I need front and back label design for about 12 different variety of products. They are all to do with the Automotive additive industry such as Petrol injector cleaner, Engine Flush, Oil treatments etc. I will provide overall measurements of the label in the brief as well as examples of artwork that I like. Label must comply with local regulations, i can assist you with this. We will start with one product only, and if successful I am happy to hire you to do the remainder of the project. I would like to see designs that use my company logo colors. These products are for the workshop industry only (not retail) so does not have to be too animated.You will see my logo designs under the name "torlux" in the uploaded files.Product Name is : Motor Clear & Renew
Front Label must say:PREPARES ENGINES FOR NEW OIL
RESTORES COMPRESSION
MINIMISES CONTAMINATION WITH NEW OIL
CONTAINS TORLUX ARMOR COAT PROTECTION
RECOMMENDED FOR PETROL, DIESEL AND HYBRID ENGINES
350ML
Dimensions of metal can that will be used for label is : 175mm in height and 56mm in diameter. IN THE UPLOADED FILES YOU WILL SEE A SAMPLE OF THE ACTUAL CAN TO BE USED.
I have now included an example of a shield/guard that should be shown on the rear of the label if possible, im happy if you come up with your own shield designs.

Target Market(s)

Mechanics

Industry/Entity Type

Automotive Part

Requirements
Must have
• My logo on top
Nice to have
• Silver background
Should not have
• Pictures of engines or engine parts etc

```html
<!DOCTYPE html>
<html lang="en">
<head>
<meta charset="utf-8">
<title>Torlux Motor Clear &amp; Renew – Front Label</title>
<link href="https://fonts.googleapis.com/css2?family=Roboto+Condensed:ital,wght@0,400;0,700;0,900;1,700;1,900&display=swap" rel="stylesheet">
<style>
  :root{
    --page:#e2e2e2;
    --silver-light:#f2f3f4;
    --silver-mid:#c9cccf;
    --silver-dark:#a7abaf;
    --band:#111214;
    --band-edge:#8d9094;
    --brand-blue:#1e4fc0;
    --brand-orange:#e8771c;
    --gold-light:#fbeaa4;
    --gold:#eac244;
    --gold-deep:#d9a925;
    --ink:#111111;
    --white:#ffffff;
  }
  *{box-sizing:border-box;margin:0;padding:0}
  html,body{width:1172px;height:1200px;overflow:hidden}
  body{background:var(--page);font-family:"Roboto Condensed",sans-serif;position:relative}

  .label{
    position:absolute;left:385px;top:130px;width:368px;height:900px;overflow:hidden;
    background:linear-gradient(90deg,var(--silver-dark) 0%,var(--silver-light) 22%,var(--silver-mid) 45%,var(--silver-light) 70%,var(--silver-dark) 100%);
  }
  .panel-lines{position:absolute;inset:0}

  .brand{position:absolute;left:0;top:70px;width:100%;text-align:center}
  .brand-mark{display:block;margin:0 auto;width:84px;height:84px;border-radius:50%;background:var(--brand-blue)}
  .brand-name{display:block;margin-top:14px;font-weight:900;font-size:40px;letter-spacing:2px;color:var(--brand-blue);line-height:1}
  .brand-tagline{display:block;margin-top:6px;font-weight:400;font-size:10px;letter-spacing:1px;color:#6a6e73}

  .product-band{
    position:absolute;left:0;top:332px;width:100%;height:90px;background:var(--band);
    border-top:2px solid var(--band-edge);border-bottom:2px solid var(--band-edge);
    display:flex;flex-direction:column;align-items:center;justify-content:center;
  }
  .product-name{
    font-style:italic;font-weight:900;font-size:38px;line-height:40px;color:var(--white);
    -webkit-text-stroke:1.5px var(--brand-blue);text-align:center;letter-spacing:-0.5px;
  }

  .gold-wave{position:absolute;left:0;top:560px;width:100%;height:340px}

  .claims{position:absolute;left:27px;top:704px;width:330px;color:var(--ink)}
  .claims-head{font-weight:900;font-size:23px;line-height:23px;letter-spacing:-0.5px;text-transform:uppercase}
  .claims-list{list-style:none;margin-top:12px}
  .claims-list li{position:relative;padding-left:16px;font-weight:700;font-style:italic;font-size:13.5px;line-height:19px;letter-spacing:-0.3px}
  .claims-list li::before{
    content:"";position:absolute;left:2px;top:6px;width:6px;height:8px;background:var(--ink);
    border-radius:50% 50% 50% 50% / 60% 60% 40% 40%;
  }
  .volume{position:absolute;left:0;top:852px;width:100%;text-align:center;font-weight:700;font-style:italic;font-size:13px;color:var(--ink)}
</style>
</head>
<body>
  <main class="label">
    <svg class="panel-lines" width="368" height="900" viewBox="0 0 368 900" aria-hidden="true">
      <g stroke="#1a1a1a" stroke-width="2" fill="none">
        <line x1="0" y1="110" x2="79" y2="0"/>
        <line x1="239" y1="0" x2="368" y2="232"/>
        <line x1="215" y1="662" x2="368" y2="478"/>
        <line x1="303" y1="558" x2="368" y2="670"/>
      </g>
    </svg>

    <div class="brand">
      <span class="brand-mark"></span>
      <span class="brand-name">TORLUX</span>
      <span class="brand-tagline">DRIVE WITH TORLUX</span>
    </div>

    <div class="product-band">
      <h1 class="product-name">MOTOR CLEAR<br>&amp; RENEW</h1>
    </div>

    <svg class="gold-wave" role="img" aria-label="Flowing golden oil swirl" width="368" height="340" viewBox="0 0 368 340" preserveAspectRatio="none">
      <defs>
        <linearGradient id="gold-fill" x1="0" y1="0" x2="1" y2="1">
          <stop offset="0" stop-color="var(--gold)"/>
          <stop offset="0.45" stop-color="var(--gold-light)"/>
          <stop offset="0.75" stop-color="var(--gold)"/>
          <stop offset="1" stop-color="var(--gold-deep)"/>
        </linearGradient>
      </defs>
      <path d="M0 40 C60 0 140 10 210 40 C270 65 320 90 368 110 L368 340 L0 340 Z" fill="url(#gold-fill)"/>
    </svg>

    <section class="claims">
      <h2 class="claims-head">Prepares Engines<br>For New Oil</h2>
      <ul class="claims-list">
        <li>Restores Compression</li>
        <li>Minimises Contamination with New Oil</li>
        <li>Contains Torlux Armor Coat Protection</li>
        <li>Recommended For Petrol, Diesel And Hybrid Engine</li>
      </ul>
    </section>

    <p class="volume">300 ml</p>
  </main>
</body>
</html>
```